Postcard Design For Thrift Store (We have Pictures)

Hey there! So we run a thrift store, and are looking to build a double sided 4 x 6 postcard mailer design (with the address on it of course). We would like the PSD file so that we may edit the design in the future.

We'd like a green background. As our store color is currently green.

There are a few things we'd like to emphasize in the copy of the postcard:

- On the top text put "Thrift Store now open" with our logo (picture of store front included has logo) below it.
- A call to action to stop by for winter clothes
- That we have brand name clothes, furniture, toys and children clothes for great prices.
- A spot that mentions that we take donations
- We have weekly sales tuesdays and thursdays
- A coupon spot that give them 20% off if they bring the postcard in. Expires 1/1/15
- That our store is next to the Bramwell in the Fernhollow shopping center

I've attached pictures that we'd like used that show the inside of the store. Plus one of the store front, as we'd like you to use the red part title below "Thrift Store" as the logo. And lastly I've attached a photo of where our store is on Google maps. I'd like that communicated with our store address.

Store number is 301-738-5196

Our store address is 48217 Quillon Rd, #207
Corvale, Ohio

```html
<!DOCTYPE html>
<html lang="en">
<head>
<meta charset="utf-8">
<title>Thrift Bin, Inc. – Postcard Mailer</title>
<link rel="stylesheet" href="https://fonts.googleapis.com/css2?family=Arimo&family=Lobster&family=Open+Sans:ital,wght@1,800&family=Oswald:wght@600&family=PT+Sans+Narrow:wght@400;700&display=swap">
<style>
  :root{
    --page:#ecebe7;
    --olive:#6b8b3d;
    --lime:#b5d25b;
    --lime-edge:#cfe397;
    --red:#d3282b;
    --ink:#2b2b2b;
    --white:#ffffff;
    --coupon:#d9d9d9;
    --quote:#c6e06a;
    --rule:#9a9a9a;
  }
  *{box-sizing:border-box;margin:0;padding:0}
  html,body{width:1200px;height:500px;overflow:hidden}
  body{background:var(--page);position:relative;font-family:"PT Sans Narrow",sans-serif;color:var(--ink)}
  .abs{position:absolute}

  /* front */
  .card-front{left:25px;top:37px;width:560px;height:433px;background:var(--lime-edge);box-shadow:0 2px 6px rgba(0,0,0,.2)}
  .front-header{left:0;top:0;width:560px;height:62px;background:var(--olive);display:flex;align-items:center;justify-content:center}
  .front-title{font-family:"Open Sans",sans-serif;font-style:italic;font-weight:800;font-size:33px;color:var(--white)}
  .storefront{left:0;top:62px;width:560px;height:75px;background:linear-gradient(90deg,#5a4a42,#8a8c8a 40%,#6b6f70 70%,#7a4c3c);display:flex;align-items:center;justify-content:center}
  .brand-name{font-family:"Oswald",sans-serif;font-weight:600;font-size:32px;color:var(--red);letter-spacing:1px}
  .front-body{left:8px;top:137px;width:544px;height:288px;background:var(--lime)}
  .weekly-title{left:12px;top:1px;font-family:"Oswald",sans-serif;font-weight:600;font-size:36px;line-height:1;color:var(--red)}
  .weekly-days{left:12px;top:40px;font-size:18px;letter-spacing:.3px}
  .location-pill{left:27px;top:61px;width:182px;height:56px;border-radius:12px;background:var(--olive);color:var(--white);font-weight:700;font-size:15px;line-height:1.15;text-align:center;display:flex;align-items:center;justify-content:center}
  .phone{left:27px;top:120px;display:flex;align-items:center;gap:4px;font-family:"Oswald",sans-serif;font-weight:600;font-size:23px;color:var(--red)}
  .prices-title{left:247px;top:20px;font-weight:700;font-size:18px}
  .prices-list{left:247px;top:43px;list-style:none;font-weight:700;font-size:16px;line-height:1.1}
  .prices-list li::before{content:"";display:inline-block;width:7px;height:7px;border-radius:50%;background:var(--red);margin-right:4px;vertical-align:2px}
  .photo{background:linear-gradient(135deg,#6b5a4c,#a99a86 50%,#4d3c34)}
  .photo-jacket{left:385px;top:6px;width:150px;height:89px}
  .photo-bags{left:385px;top:98px;width:150px;height:90px}
  .photo-coats{left:385px;top:191px;width:150px;height:88px;background:linear-gradient(135deg,#8a6e4f,#b77a5a 50%,#4f5a3a)}
  .coupon{left:-8px;top:146px;width:150px;height:137px;background:var(--coupon);border:2px dashed var(--white);text-align:center;padding-top:6px}
  .coupon-value{font-family:"Oswald",sans-serif;font-weight:600;font-size:38px;line-height:1.05;color:var(--red)}
  .coupon-terms{font-weight:700;font-size:16px;line-height:1.05;margin-top:2px}
  .coupon-expiry{font-weight:700;font-size:12px;margin-top:12px}
  .photo-interior{left:142px;top:148px;width:240px;height:135px;background:linear-gradient(180deg,#e8e6e0 0%,#b9b3aa 40%,#6b5e58 75%,#4a3f3a)}
  .cta-script{left:146px;top:158px;font-family:"Lobster",cursive;font-size:29px;line-height:1;color:var(--red);transform:rotate(-7deg);transform-origin:left center;white-space:nowrap;letter-spacing:1px;text-shadow:0 0 3px rgba(255,255,255,.7)}
  .donation-badge{left:358px;top:225px;width:64px;height:64px;border-radius:50%;background:var(--red);color:var(--white);font-weight:700;font-size:12px;line-height:1.1;display:flex;align-items:center;justify-content:center;text-align:center;border:2px solid var(--white)}

  /* back */
  .card-back{left:617px;top:37px;width:538px;height:433px;background:var(--white);border:1px solid #bdbdbd;box-shadow:0 2px 6px rgba(0,0,0,.2)}
  .back-photo{left:0;top:0;width:270px;height:176px;background:linear-gradient(180deg,#6c8a3e 0%,#6c8a3e 12%,#6b6f72 45%,#3a3e42)}
  .tagline{left:6px;top:26px;font-family:"Lobster",cursive;font-size:18px;line-height:1;letter-spacing:1px;color:var(--white)}
  .back-brand{left:48px;top:70px;font-family:"Oswald",sans-serif;font-weight:600;font-size:20px;color:var(--red)}
  .quote{right:16px;top:117px;text-align:right;font-weight:700;font-size:19px;line-height:1.05;color:var(--quote)}
  .quote-author{display:block;font-size:13px;margin-top:3px;padding-right:24px}
  .map{left:0;top:176px;width:270px;height:180px;background:linear-gradient(160deg,#efe7d6,#f4ecd9 60%,#e8e0cd)}
  .sender-brand{left:288px;top:27px;width:116px;height:22px;background:#2d2d2d;display:flex;align-items:center;justify-content:center;font-family:"Oswald",sans-serif;font-weight:600;font-size:12px;color:var(--red)}
  .sender-address{left:280px;top:57px;width:132px;text-align:center;font-family:"Arimo",sans-serif;font-size:12px;line-height:1.3;color:var(--ink)}
  .stamp-box{left:416px;top:26px;width:94px;height:120px;border:1px solid var(--rule)}
  .address-line{left:298px;width:240px;height:1px;background:var(--rule)}
</style>
</head>
<body>

<section class="card-front abs" aria-label="Postcard front">
  <header class="front-header abs"><h1 class="front-title">Thrift Store Now Open!</h1></header>
  <div class="storefront abs" role="img" aria-label="Photo of the store front with its sign">
    <span class="brand-name">THRIFT BIN, INC.</span>
  </div>

  <div class="front-body abs">
    <h2 class="weekly-title abs">WEEKLY SALES</h2>
    <p class="weekly-days abs">EVERY TUESDAY &amp; THURSDAY</p>
    <p class="location-pill abs">Our store is located<br>next to the Bramwell in the<br>Fernhollow Shopping Center</p>
    <p class="phone abs">
      <svg width="22" height="22" viewBox="0 0 24 24" aria-hidden="true"><circle cx="12" cy="12" r="10.5" fill="none" stroke="#d3282b" stroke-width="2"/><path d="M9 6.5c-.8 0-1.6 1-1.6 2 0 3.6 3.5 8.5 7.4 9.2 1 .2 2-.5 2.2-1.3l-2-1.8-1.4.8c-1.5-.7-2.8-2.4-3.2-3.9l1.2-1-.9-2.5z" fill="#d3282b"/></svg>
      301.738.5196
    </p>

    <h3 class="prices-title abs">GREAT PRICES ON:</h3>
    <ul class="prices-list abs">
      <li>Brand name clothes</li>
      <li>Furniture</li>
      <li>Toys</li>
      <li>Children clothes</li>
    </ul>

    <div class="photo photo-jacket abs" role="img" aria-label="Photo of leather jackets on a rack"></div>
    <div class="photo photo-bags abs" role="img" aria-label="Photo of handbags on a shelf"></div>
    <div class="photo photo-coats abs" role="img" aria-label="Photo of winter coats on hangers"></div>

    <div class="photo-interior abs" role="img" aria-label="Photo of the store interior with clothing racks"></div>
    <p class="cta-script abs">Stop by for winter clothes</p>

    <div class="coupon abs">
      <p class="coupon-value">20% OFF</p>
      <p class="coupon-terms">IF YOU BRING THIS<br>POSTCARD</p>
      <p class="coupon-expiry">PROMO EXPIRES 1/1/15</p>
    </div>

    <p class="donation-badge abs">WE TAKE<br>DONATIONS</p>
  </div>
</section>

<section class="card-back abs" aria-label="Postcard back">
  <div class="back-photo abs" role="img" aria-label="Photo of the store front">
    <p class="tagline abs">Fabulous Clothing For Less!</p>
    <p class="back-brand abs">THRIFT BIN, INC.</p>
    <p class="quote abs">Thrift is essential to<br>well-ordered living.<span class="quote-author">Harold W. Penbrook</span></p>
  </div>
  <div class="map abs" role="img" aria-label="Map showing the store location at 48217 Quillon Rd, #207, Corvale, near the Fernhollow Shopping Center"></div>

  <p class="sender-brand abs">THRIFT BIN, INC.</p>
  <p class="sender-address abs">48217 Quillon Rd, #207<br>Corvale, Ohio<br>USA</p>
  <div class="stamp-box abs" aria-label="Stamp area"></div>

  <div class="address-line abs" style="top:228px"></div>
  <div class="address-line abs" style="top:262px"></div>
  <div class="address-line abs" style="top:298px"></div>
  <div class="address-line abs" style="top:333px"></div>
</section>

</body>
</html>
```